Design interface for an invoicing software

We are developing a new invoicing software that is a very boring topic. Users can use the software to write invoices and manage their income. Therefore we want to inspire the users with a great desgin. By this we mean, for example, the use of photos in the background (streets in New York, landscapes), or "crazy" looking headlines or something else. Target group are young start-ups, freelancers, hairdressers and taxi drivers at the age of 18-40 years. It would also be worth considering to adapt the look to the user's industry. However, the menu items themselves and the approximate position of the information are given. See file "startpoint" What kind of ideas do you have?

Europe

Small Business

Designer to choose colors to be used in the design.

• the menu items themselves and the approximate position of the information are given. The navigation menu itself can be different.
• boring look and feel

```html
<!DOCTYPE html>
<html lang="en">
<head>
<meta charset="utf-8">
<title>Invoicing App Screens</title>
<link rel="stylesheet" href="https://fonts.googleapis.com/css2?family=Mulish:wght@400;600;700;800;900&display=swap">
<style>
:root{
  --ink:#111;
  --navy:#14215a;
  --muted:#b7b7b7;
  --label:#555;
  --surface:#f4f4f4;
  --panel:#efefef;
  --lavender:#e8d6e8;
  --violet:#6a2ee6;
  --blue:#4aa3e0;
  --pink:#ff1f9a;
  --rose:#ff7fa6;
  --green:#20c51f;
  --lock:#ff2f8a;
  --line:#dcdcdc;
}
*{box-sizing:border-box;margin:0;padding:0}
html,body{width:1200px;height:926px;overflow:hidden}
body{font-family:"Mulish",sans-serif;color:var(--ink);background:#fff;position:relative}
.backdrop-band{position:absolute;left:0;top:525px;width:1200px;height:401px;background:var(--lavender)}
.screen{position:absolute;top:78px;width:337px;height:730px;background:#fff;overflow:hidden;box-shadow:0 10px 22px rgba(0,0,0,.14)}
.screen--dashboard{left:80px}
.screen--invoices{left:439px;background:var(--panel)}
.screen--banking{left:802px}
.abs{position:absolute}
.status-time{position:absolute;left:27px;top:10px;font-size:14px;font-weight:600}
.status-icons{position:absolute;right:26px;top:12px}
.nav-title{position:absolute;top:59px;left:0;width:100%;text-align:center;font-size:15px;font-weight:800}
.nav-back{position:absolute;left:26px;top:62px}
.nav-lock{position:absolute;right:26px;top:59px}
.app-header{position:absolute;left:0;top:0;width:100%;height:105px;background:#fff;box-shadow:0 2px 6px rgba(0,0,0,.06);z-index:2}

/* dashboard */
.balance-panel{position:absolute;left:0;top:105px;width:100%;height:133px;background:var(--surface)}
.balance-label{position:absolute;left:27px;top:25px;font-size:11px;color:var(--label);font-weight:600}
.balance-currency{position:absolute;left:26px;top:58px;font-size:12px;font-weight:800;color:var(--navy)}
.balance-amount{position:absolute;left:42px;top:50px;font-size:38px;font-weight:900;color:var(--navy);letter-spacing:.5px}
.balance-caret{position:absolute;left:210px;top:70px}
.balance-trend{position:absolute;left:259px;top:102px;font-size:11px;font-weight:800;color:var(--green)}
.balance-trend-arrow{position:absolute;left:296px;top:99px}
.panel-notch{position:absolute;left:292px;top:238px;width:0;height:0;border-left:8px solid transparent;border-right:8px solid transparent;border-top:8px solid var(--surface)}
.menu-item{position:absolute;left:25px;height:30px;display:flex;align-items:center;gap:16px;font-size:15px;font-weight:700;color:var(--muted)}
.menu-item svg{width:24px;height:24px}
.menu-item--active{left:0;top:338px;width:190px;height:51px;padding-left:27px;border-radius:0 26px 26px 0;background:linear-gradient(90deg,var(--violet),var(--blue));color:#fff;box-shadow:0 8px 16px rgba(74,120,230,.35)}
.mini-preview{position:absolute;left:235px;top:284px;width:102px;height:356px;background:var(--panel)}
.mini-header{position:absolute;left:0;top:0;width:100%;height:50px;background:linear-gradient(120deg,var(--violet),var(--blue));color:#fff}
.mini-tab{position:absolute;top:50px;height:26px;font-size:6px;font-weight:800;color:#fff;display:flex;align-items:center;justify-content:center}
.mini-card{position:absolute;left:13px;width:95px;height:35px;background:#fff;box-shadow:0 1px 3px rgba(0,0,0,.08)}
.mini-card b{position:absolute;left:22px;top:11px;font-size:7px;font-weight:700;color:#444}
.mini-card i{position:absolute;left:22px;top:21px;font-size:4px;font-style:normal;color:#777;white-space:nowrap}
.mini-card .mini-avatar{position:absolute;left:6px;top:10px}
.logout{position:absolute;left:242px;top:685px;display:flex;align-items:center;gap:8px;font-size:11px;font-weight:800;color:var(--navy)}

/* invoices */
.invoices-header{position:absolute;left:0;top:0;width:100%;height:105px;background:linear-gradient(110deg,#6630e4 0%,#4f8be0 60%,#48a3e0 100%);color:#fff}
.invoices-header .status-time,.invoices-header .nav-title{color:#fff}
.tab{position:absolute;top:105px;height:55px;width:169px;display:flex;align-items:center;justify-content:center;font-size:14px;font-weight:700;color:#fff}
.tab--active{left:0;background:linear-gradient(90deg,var(--pink),var(--rose))}
.tab--idle{left:169px;width:168px;background:linear-gradient(90deg,#7f7fe0,#6aaee0)}
.tab-notch{position:absolute;left:77px;top:160px;border-left:7px solid transparent;border-right:7px solid transparent;border-top:7px solid #ff4aa2}
.invoice-card{position:absolute;left:27px;width:283px;height:72px;background:#fff;box-shadow:0 3px 10px rgba(0,0,0,.06)}
.invoice-card .avatar{position:absolute;left:10px;top:18px}
.invoice-name{position:absolute;left:47px;top:22px;font-size:16px;font-weight:700;color:#555}
.invoice-dates{position:absolute;left:47px;top:42px;font-size:9px;color:#666;white-space:nowrap}
.invoice-dates span{margin-left:10px}
.invoice-amount{position:absolute;right:14px;top:18px;width:53px;height:36px;display:flex;align-items:center;justify-content:center;font-size:10px;font-weight:700;color:#fff;border-radius:2px}
.amount--due{background:linear-gradient(135deg,var(--violet),var(--blue))}
.amount--late{background:linear-gradient(135deg,var(--pink),var(--rose))}
.invoice-draft{position:absolute;left:27px;top:572px;width:283px;height:72px;border:1.5px dashed #c8c8c8}

/* banking */
.ssl-note{font-size:9px;font-weight:600;margin-left:3px}
.method-panel{position:absolute;left:0;top:105px;width:100%;height:153px;background:var(--surface)}
.section-label{position:absolute;left:27px;font-size:11px;font-weight:600;color:#444}
.method-tile{position:absolute;top:64px;width:85px;height:54px;display:flex;align-items:center;justify-content:center;font-size:15px;font-weight:800;color:#c4c4c4}
.method--card{left:27px;background:linear-gradient(135deg,var(--violet),var(--blue))}
.method--wallet{left:127px;border:2px solid #dadada;background:#f1f1f1}
.method--store{left:226px;background:#fff}
.method-check{position:absolute;left:83px;top:112px;width:18px;height:18px;border-radius:50%;background:#fff;box-shadow:0 1px 3px rgba(0,0,0,.2);display:flex;align-items:center;justify-content:center}
.field{position:absolute;left:27px;width:283px;height:57px;border:2px solid var(--line);background:#fff}
.field--filled{background:#f2f2f2}
.field-label{position:absolute;left:13px;top:12px;font-size:8px;font-weight:600;color:#777;letter-spacing:.3px}
.field-value{position:absolute;left:13px;top:28px;font-size:13px;font-weight:800}
.field-split{position:absolute;left:141px;top:0;width:2px;height:100%;background:var(--line)}
.field-valid{position:absolute;left:292px;top:424px;width:17px;height:17px;background:var(--green);border-radius:2px;display:flex;align-items:center;justify-content:center}
.field-help{position:absolute;left:297px;top:474px;width:17px;height:17px;border-radius:50%;background:#e4e4e4;font-size:10px;font-weight:900;display:flex;align-items:center;justify-content:center}
.remember-label{position:absolute;left:26px;top:580px;font-size:11px;font-weight:600;color:#333}
.toggle{position:absolute;left:256px;top:573px;width:54px;height:27px;border-radius:14px;background:linear-gradient(90deg,var(--violet),var(--blue));box-shadow:0 5px 12px rgba(90,90,230,.4)}
.toggle::after{content:"";position:absolute;right:5px;top:5px;width:17px;height:17px;border-radius:50%;background:#fff;box-shadow:inset 0 0 0 5px #fff,inset 0 0 0 8px #333}
.buy-button{position:absolute;left:27px;top:649px;width:283px;height:54px;border-radius:27px;background:linear-gradient(90deg,#ff8cab,var(--pink) 60%,#ff1a96);box-shadow:0 8px 18px rgba(255,40,150,.35);color:#fff;font-size:14px;font-weight:800;display:flex;align-items:center;justify-content:center;letter-spacing:.3px}
.buy-icon{position:absolute;left:9px;top:9px;width:36px;height:36px;border-radius:50%;background:#fff;display:flex;align-items:center;justify-content:center}
</style>
</head>
<body>
<div class="backdrop-band"></div>

<section class="screen screen--dashboard">
  <header class="app-header">
    <div class="status-time">9:41</div>
    <svg class="status-icons" width="50" height="12" viewBox="0 0 50 12"><rect x="0" y="8" width="2.5" height="3"/><rect x="4" y="6" width="2.5" height="5"/><rect x="8" y="4" width="2.5" height="7"/><rect x="12" y="2" width="2.5" height="9"/><path d="M18 4a9 9 0 0 1 12 0l-1.5 1.6a7 7 0 0 0-9 0zM20.5 6.7a5 5 0 0 1 7 0L24 11z"/><rect x="33" y="1.5" width="15" height="9" rx="2" fill="none" stroke="#000" stroke-width="1.2"/><rect x="35" y="3.5" width="11" height="5" rx="1"/></svg>
    <svg class="nav-back" width="20" height="12" viewBox="0 0 20 12"><path d="M19 6H2M6 1 1 6l5 5" fill="none" stroke="#6a2ee6" stroke-width="2"/></svg>
    <h1 class="nav-title">Dashboard</h1>
    <svg class="nav-lock" width="14" height="17" viewBox="0 0 14 17"><path d="M3.5 7V4.5a3.5 3.5 0 0 1 7 0V7" fill="none" stroke="#ff2f8a" stroke-width="2"/><rect y="7" width="14" height="10" rx="1.5" fill="#ff2f8a"/><rect x="6" y="10" width="2" height="4" fill="#fff"/></svg>
  </header>
  <div class="balance-panel">
    <div class="balance-label">Account Balance</div>
    <div class="balance-currency">$</div>
    <div class="balance-amount">4586.99</div>
    <svg class="balance-caret" width="8" height="6" viewBox="0 0 8 6"><path d="M1 1l3 3 3-3" fill="none" stroke="#14215a" stroke-width="1.6"/></svg>
    <div class="balance-trend">+15%</div>
    <svg class="balance-trend-arrow" width="13" height="13" viewBox="0 0 13 13"><path d="M1 12 12 1M4 1h8v8" fill="none" stroke="#20c51f" stroke-width="1.6"/></svg>
  </div>
  <div class="panel-notch"></div>

  <nav>
    <div class="menu-item" style="top:291px"><svg viewBox="0 0 24 24"><circle cx="12" cy="7" r="5" fill="#bcbcbc"/><path d="M2 24c0-6 4-10 10-10s10 4 10 10z" fill="#bcbcbc"/></svg>Contacts</div>
    <div class="menu-item menu-item--active"><svg viewBox="0 0 24 24"><path d="M4 1h16v22l-3-2-2 2-3-2-3 2-2-2-3 2z" fill="#fff"/><text x="12" y="11" font-size="8" text-anchor="middle" fill="#6a6ae6" font-family="Mulish,sans-serif" font-weight="800">$</text><rect x="7" y="14" width="10" height="1.6" fill="#6a6ae6"/><rect x="7" y="17" width="10" height="1.6" fill="#6a6ae6"/></svg>Invoices</div>
    <div class="menu-item" style="top:418px"><svg viewBox="0 0 24 24"><path d="M0 3h4l3 12h13l3-9H6" fill="none" stroke="#bcbcbc" stroke-width="2"/><circle cx="9" cy="20" r="2" fill="#bcbcbc"/><circle cx="18" cy="20" r="2" fill="#bcbcbc"/><rect x="8" y="8" width="12" height="5" fill="#d4d4d4"/></svg>Products</div>
    <div class="menu-item" style="top:471px"><svg viewBox="0 0 24 24"><path d="M12 1 1 7h22z" fill="#bcbcbc"/><rect x="3" y="9" width="3" height="10" fill="#bcbcbc"/><rect x="8" y="9" width="3" height="10" fill="#bcbcbc"/><rect x="13" y="9" width="3" height="10" fill="#bcbcbc"/><rect x="18" y="9" width="3" height="10" fill="#bcbcbc"/><rect x="1" y="20" width="22" height="3" fill="#bcbcbc"/></svg>Banking</div>
    <div class="menu-item" style="top:524px"><svg viewBox="0 0 24 24"><rect x="4" y="4" width="19" height="14" rx="2" fill="#bcbcbc"/><rect x="14" y="8" width="9" height="6" fill="#d8d8d8"/><circle cx="5" cy="18" r="5" fill="#9a9a9a"/><rect x="2.5" y="17.2" width="5" height="1.6" fill="#fff"/></svg>Expenses</div>
    <div class="menu-item" style="top:577px"><svg viewBox="0 0 24 24"><rect x="1" y="1" width="22" height="22" fill="none" stroke="#bcbcbc" stroke-width="2"/><path d="M4 14l5-5 4 4 7-7" fill="none" stroke="#bcbcbc" stroke-width="2"/><rect x="4" y="17" width="16" height="1.5" fill="#bcbcbc"/></svg>Reports</div>
  </nav>

  <div class="mini-preview">
    <div class="mini-header">
      <span class="abs" style="left:13px;top:6px;font-size:6px">9:41</span>
      <span class="abs" style="left:16px;top:26px;font-size:12px">+</span>
      <span class="abs" style="left:64px;top:30px;font-size:7px;font-weight:800">Invoices</span>
    </div>
    <div class="mini-tab" style="left:0;width:84px;background:linear-gradient(90deg,#ff2f9a,#ff7fa6)">Must Pay</div>
    <div class="mini-tab" style="left:84px;width:18px;background:#7f82e0"></div>
    <div class="mini-card" style="top:100px"><svg class="mini-avatar" width="10" height="12" viewBox="0 0 10 12"><circle cx="5" cy="3" r="3" fill="#aaa"/><path d="M0 12c0-3 2-5 5-5s5 2 5 5z" fill="#aaa"/></svg><b>Nora Halden</b><i>Date 17/09/18 Due Date 17/09</i></div>
    <div class="mini-card" style="top:142px"><svg class="mini-avatar" width="10" height="12" viewBox="0 0 10 12"><circle cx="5" cy="3" r="3" fill="#aaa"/><path d="M0 12c0-3 2-5 5-5s5 2 5 5z" fill="#aaa"/></svg><b>Leo Halden</b><i>Date 12/09/18 Due Date 20/09</i></div>
    <div class="mini-card" style="top:185px"><svg class="mini-avatar" width="10" height="12" viewBox="0 0 10 12"><circle cx="5" cy="3" r="3" fill="#aaa"/><path d="M0 12c0-3 2-5 5-5s5 2 5 5z" fill="#aaa"/></svg><b>Leo Marsh</b><i>Date 05/09/18 Due Date 11/09</i></div>
    <div class="mini-card" style="top:227px"><svg class="mini-avatar" width="10" height="12" viewBox="0 0 10 12"><circle cx="5" cy="3" r="3" fill="#aaa"/><path d="M0 12c0-3 2-5 5-5s5 2 5 5z" fill="#aaa"/></svg><b>Nora Halden</b><i>Date 17/09/18 Due Date 17/09</i></div>
    <div class="mini-card" style="top:279px;background:none;box-shadow:none;border:1px dashed #bbb"><svg class="abs" style="left:8px;top:9px" width="42" height="16" viewBox="0 0 42 16"><circle cx="8" cy="8" r="8" fill="#ccc"/><circle cx="8" cy="8" r="2.5" fill="#eee"/><rect x="22" y="4" width="20" height="4" fill="#ccc"/><rect x="22" y="10" width="12" height="3" fill="#ccc"/></svg></div>
  </div>

  <div class="logout"><svg width="18" height="18" viewBox="0 0 18 18"><path d="M7 1H1v16h6M6 9h11M13 5l4 4-4 4" fill="none" stroke="#111" stroke-width="1.6"/></svg>Log Out</div>
</section>

<section class="screen screen--invoices">
  <header class="invoices-header">
    <div class="status-time">9:41</div>
    <svg class="status-icons" width="50" height="12" viewBox="0 0 50 12" fill="#fff"><rect x="0" y="8" width="2.5" height="3"/><rect x="4" y="6" width="2.5" height="5"/><rect x="8" y="4" width="2.5" height="7"/><rect x="12" y="2" width="2.5" height="9"/><path d="M18 4a9 9 0 0 1 12 0l-1.5 1.6a7 7 0 0 0-9 0zM20.5 6.7a5 5 0 0 1 7 0L24 11z"/><rect x="33" y="1.5" width="15" height="9" rx="2" fill="none" stroke="#fff" stroke-width="1.2"/><rect x="35" y="3.5" width="11" height="5" rx="1"/></svg>
    <svg class="abs" style="left:27px;top:60px" width="18" height="18" viewBox="0 0 18 18"><path d="M9 0v18M0 9h18" stroke="#fff" stroke-width="2"/></svg>
    <h1 class="nav-title" style="font-size:17px;font-weight:700;top:57px">Invoices</h1>
    <svg class="abs" style="left:291px;top:61px" width="19" height="16" viewBox="0 0 19 16"><path d="M0 1h19M5 8h14M3 15h16" stroke="#fff" stroke-width="1.8"/></svg>
  </header>
  <div class="tab tab--active">Must Pay</div>
  <div class="tab tab--idle">Paid</div>
  <div class="tab-notch"></div>

  <article class="invoice-card" style="top:204px">
    <svg class="avatar" width="28" height="34" viewBox="0 0 28 34"><circle cx="14" cy="8" r="8" fill="#bbb"/><path d="M0 34c0-9 6-15 14-15s14 6 14 15z" fill="#bbb"/></svg>
    <div class="invoice-name">Nora Halden</div>
    <div class="invoice-dates">Date 17/09/18 <span>Due Date 17/09/18</span></div>
    <div class="invoice-amount amount--due">$264.00</div>
  </article>
  <article class="invoice-card" style="top:291px">
    <svg class="avatar" width="28" height="34" viewBox="0 0 28 34"><circle cx="14" cy="8" r="8" fill="#bbb"/><path d="M0 34c0-9 6-15 14-15s14 6 14 15z" fill="#bbb"/></svg>
    <div class="invoice-name">Leo Halden</div>
    <div class="invoice-dates">Date 12/09/18 <span>Due Date 20/09/18</span></div>
    <div class="invoice-amount amount--late">$127.80</div>
  </article>
  <article class="invoice-card" style="top:378px">
    <svg class="avatar" width="28" height="34" viewBox="0 0 28 34"><circle cx="14" cy="8" r="8" fill="#bbb"/><path d="M0 34c0-9 6-15 14-15s14 6 14 15z" fill="#bbb"/></svg>
    <div class="invoice-name">Leo Marsh</div>
    <div class="invoice-dates">Date 05/09/18 <span>Due Date 11/09/18</span></div>
    <div class="invoice-amount amount--due">$56.05</div>
  </article>
  <article class="invoice-card" style="top:464px">
    <svg class="avatar" width="28" height="34" viewBox="0 0 28 34"><circle cx="14" cy="8" r="8" fill="#bbb"/><path d="M0 34c0-9 6-15 14-15s14 6 14 15z" fill="#bbb"/></svg>
    <div class="invoice-name">Nora Halden</div>
    <div class="invoice-dates">Date 17/09/18 <span>Due Date 17/09/18</span></div>
    <div class="invoice-amount amount--late">$264.00</div>
  </article>
  <div class="invoice-draft">
    <svg class="abs" style="left:18px;top:18px" width="100" height="36" viewBox="0 0 100 36"><circle cx="18" cy="18" r="18" fill="#d0d0d0"/><circle cx="18" cy="18" r="5" fill="#ececec"/><rect x="53" y="6" width="45" height="12" fill="#d0d0d0"/><rect x="53" y="23" width="27" height="7" fill="#d0d0d0"/></svg>
    <svg class="abs" style="left:201px;top:17px" width="64" height="36" viewBox="0 0 64 36"><rect width="64" height="36" rx="2" fill="#d0d0d0"/><rect x="20" y="15" width="24" height="7" rx="1" fill="#f2f2f2"/></svg>
  </div>
</section>

<section class="screen screen--banking">
  <header class="app-header">
    <div class="status-time">9:41</div>
    <svg class="status-icons" width="50" height="12" viewBox="0 0 50 12"><rect x="0" y="8" width="2.5" height="3"/><rect x="4" y="6" width="2.5" height="5"/><rect x="8" y="4" width="2.5" height="7"/><rect x="12" y="2" width="2.5" height="9"/><path d="M18 4a9 9 0 0 1 12 0l-1.5 1.6a7 7 0 0 0-9 0zM20.5 6.7a5 5 0 0 1 7 0L24 11z"/><rect x="33" y="1.5" width="15" height="9" rx="2" fill="none" stroke="#000" stroke-width="1.2"/><rect x="35" y="3.5" width="11" height="5" rx="1"/></svg>
    <svg class="nav-back" width="20" height="12" viewBox="0 0 20 12"><path d="M19 6H2M6 1 1 6l5 5" fill="none" stroke="#6a2ee6" stroke-width="2"/></svg>
    <h1 class="nav-title">Banking<span class="ssl-note">SSL Secure_</span></h1>
    <svg class="nav-lock" width="14" height="17" viewBox="0 0 14 17"><path d="M3.5 7V4.5a3.5 3.5 0 0 1 7 0V7" fill="none" stroke="#ff2f8a" stroke-width="2"/><rect y="7" width="14" height="10" rx="1.5" fill="#ff2f8a"/><rect x="6" y="10" width="2" height="4" fill="#fff"/></svg>
  </header>
  <div class="method-panel">
    <div class="section-label" style="top:25px">•&nbsp; Select your method</div>
    <div class="method-tile method--card"><svg width="32" height="24" viewBox="0 0 32 24"><g transform="rotate(-15 16 12)" fill="none" stroke="#fff" stroke-width="1.6"><rect x="4" y="2" width="22" height="14" rx="2"/><rect x="8" y="7" width="22" height="14" rx="2" fill="#7a68e6"/><path d="M8 12h22"/></g></svg></div>
    <div class="method-check"><svg width="9" height="7" viewBox="0 0 9 7"><path d="M1 3.5 3.5 6 8 1" fill="none" stroke="#20c51f" stroke-width="1.6"/></svg></div>
    <div class="method-tile method--wallet">Zavrel</div>
    <div class="method-tile method--store">Ombrix</div>
  </div>

  <div class="section-label" style="top:291px">•&nbsp; Enter your payment details</div>
  <div class="field" style="top:328px"><span class="field-label">CARDHOLDER NAME</span><span class="field-value">Marc Dorian</span></div>
  <div class="field field--filled" style="top:404px"><span class="field-label">CARD NUMBER</span><span class="field-value" style="letter-spacing:1px">●●●●&nbsp;&nbsp; ●●●●&nbsp;&nbsp; ●●●●&nbsp;&nbsp; 1234</span></div>
  <div class="field-valid"><svg width="9" height="7" viewBox="0 0 9 7"><path d="M1 3.5 3.5 6 8 1" fill="none" stroke="#fff" stroke-width="1.6"/></svg></div>
  <div class="field" style="top:480px">
    <span class="field-label">EXPIRATION DATE</span><span class="field-value">10 / 19</span>
    <span class="field-split"></span>
    <span class="field-label" style="left:154px">CVV</span><span class="field-value" style="left:154px">●●●</span>
  </div>
  <div class="field-help">?</div>

  <div class="remember-label">Remember my card details</div>
  <div class="toggle"></div>

  <div class="buy-button">
    <span class="buy-icon"><svg width="16" height="12" viewBox="0 0 16 12"><path d="M0 6h14M9 1l5 5-5 5" fill="none" stroke="#111" stroke-width="2"/></svg></span>
    BUY NOW
  </div>
</section>
</body>
</html>
```